Antibacterial Hand Wash Squeeze Tube Label

We're looking for a contemporary label design for a new Antibacterial Hand Wash for an 8oz squeeze tube. The new consumer brand will be sold to consumers in major US retail stores & online. The moisturizing hand wash contains Aloe Vera, vitamin E, and other natural ingredients so the design should include the color green. Real photos are very effective on packaging, so a picture of Aloe Vera or possibly two hands washing would help draw consumers' attention to the tube on the retail shelf. The front label may wrap around the sides. Rear must be left mostly blank
Target Market(s)
US Consumers - retail stores & online
Industry/Entity Type
Consumer

```html
<!DOCTYPE html>
<html lang="en">
<head>
<meta charset="utf-8">
<title>Veralux Moisturizing Hand Wash – Tube Label</title>
<link rel="stylesheet" href="https://fonts.googleapis.com/css2?family=Montserrat:wght@600;700;800&family=Questrial&display=swap">
<style>
  :root {
    --page: #eef1f1;
    --green: #1e9a2c;
    --green-dark: #0f6e1c;
    --green-light: #3dbb47;
    --silver-light: #ffffff;
    --silver-mid: #d9dbdc;
    --silver-dark: #9a9c9e;
    --ink: #111111;
    --white: #ffffff;
  }
  * { box-sizing: border-box; margin: 0; padding: 0; }
  html, body { width: 1200px; height: 720px; overflow: hidden; }
  body {
    background: var(--page);
    font-family: "Questrial", sans-serif;
    color: var(--ink);
    position: relative;
  }
  .label {
    position: absolute;
    top: 50px;
    width: 440px;
    height: 620px;
    overflow: hidden;
    background: linear-gradient(90deg, var(--silver-dark) 0%, var(--silver-mid) 22%, var(--silver-light) 50%, var(--silver-mid) 78%, var(--silver-dark) 100%);
    box-shadow: 0 8px 24px rgba(0,0,0,0.12);
  }
  .label--back { left: 120px; }
  .label--front { left: 640px; }
  .band {
    position: absolute;
    left: 0; right: 0;
    height: 18px;
    background: linear-gradient(180deg, var(--green-light), var(--green));
  }
  .band--top { top: 0; }
  .band--bottom { bottom: 0; }

  /* Back panel */
  .back-title {
    position: absolute;
    top: 46px; left: 0; right: 0;
    text-align: center;
    font-family: "Montserrat", sans-serif;
    font-weight: 700;
    font-size: 22px;
  }
  .benefits {
    position: absolute;
    top: 104px; left: 70px;
    list-style: none;
    font-size: 33px;
    line-height: 1.22;
  }
  .benefits li { position: relative; padding-left: 28px; }
  .benefits li::before {
    content: "";
    position: absolute;
    left: 0; top: 17px;
    width: 8px; height: 8px;
    border-radius: 50%;
    background: var(--ink);
  }
  .back-photo {
    position: absolute;
    left: 18px; right: 18px; bottom: 30px;
    height: 150px;
    border-radius: 6px;
    background: linear-gradient(100deg, #b8d6e2 0%, #dfe8ec 35%, #7fb86a 70%, #2f8f36 100%);
  }

  /* Front panel */
  .front-corner {
    position: absolute;
    top: 18px; left: 0;
    width: 150px; height: 170px;
  }
  .corner-text {
    position: absolute;
    top: 70px; left: 6px;
    color: var(--white);
    font-size: 13px;
    line-height: 1.15;
  }
  .product-tag {
    position: absolute;
    top: 90px; left: 150px;
    padding: 8px 18px;
    background: var(--green);
    border: 3px solid var(--white);
    outline: 2px solid var(--green);
    color: var(--white);
    font-family: "Montserrat", sans-serif;
    font-weight: 700;
    font-size: 26px;
    letter-spacing: 0.5px;
  }
  .swoosh {
    position: absolute;
    top: 150px; left: 0;
    width: 440px; height: 140px;
  }
  .brand {
    position: absolute;
    top: 300px; left: 0; right: 0;
    text-align: center;
    font-family: "Montserrat", sans-serif;
    font-weight: 800;
    font-size: 66px;
    letter-spacing: 1px;
  }
  .front-photo {
    position: absolute;
    right: 18px; bottom: 30px;
    width: 300px; height: 190px;
    border-radius: 6px;
    background: radial-gradient(ellipse at 60% 60%, #3c9f2c 0%, #6cbf4c 45%, rgba(200,220,200,0.4) 100%);
  }
</style>
</head>
<body>

  <section class="label label--back" aria-label="Back label">
    <div class="band band--top"></div>
    <h2 class="back-title">Moisturizing Hand Wash</h2>
    <ul class="benefits">
      <li>Antibacterial</li>
      <li>Moisturizing</li>
      <li>Aloe Vera</li>
      <li>Vitamin E</li>
      <li>Other natural<br>ingredients</li>
    </ul>
    <div class="back-photo" role="img" aria-label="Photo of a water splash, sliced aloe vera leaves and hands washing with soap"></div>
    <div class="band band--bottom"></div>
  </section>

  <section class="label label--front" aria-label="Front label">
    <div class="band band--top"></div>
    <svg class="front-corner" viewBox="0 0 150 170" aria-hidden="true">
      <polygon points="0,0 150,0 0,170" fill="var(--green)"/>
    </svg>
    <p class="corner-text">Imported<br>Formula</p>
    <div class="product-tag">HAND WASH</div>
    <svg class="swoosh" viewBox="0 0 440 140" aria-hidden="true">
      <path d="M0 130 C 120 120, 200 20, 440 10" fill="none" stroke="var(--green)" stroke-width="10"/>
    </svg>
    <h1 class="brand">VERALUX</h1>
    <div class="front-photo" role="img" aria-label="Photo of an aloe vera plant in a green liquid splash"></div>
    <div class="band band--bottom"></div>
  </section>

</body>
</html>
```